Zanquorra Business Card Design

Zanquorra is a small and new restaurant/ bar location in Hong Kong. The name "Djibouti" derives from an African country. There is no specific reason behind other than the fact, that the bar is somewhat inspired by African elements (only inspired but not purely based on African cuisine etc.).

The bar is somewhat a fusion of African, Mediterranean and Oriental (Old French Vietnam) elements.

However, it is very imperative to stress, that the overall look and feel of Zanquorra is a very high end cocktail lounge/ bar location. The bar is tucked away in a hidden alley, so people will have to know about it. The idea is to send the consumer off in an Escape or hidden remote location where they are at ease in a hip, stylish and trendy environment.

The card needs to feel high-end.

Final logo artwork has been attached and also pictures of the bar/ restaurant itself. The logo ie monkey head cannot be modified. However, the background color and the color of the type "ZANQUORRA" can be changed.

The following details need to fit onto the business card. Of course they can be arranged to your liking:

LOGO

Colin Vey
Partner

+852 97035164
xxx@zanquorra.com
www.zanquorra.com
7C, Brennick Road, Wan Chai, Hong Kong

```html
<!DOCTYPE html>
<html lang="en">
<head>
<meta charset="utf-8">
<title>Zanquorra Business Card</title>
<link href="https://fonts.googleapis.com/css2?family=Gelasio:wght@400;700&display=swap" rel="stylesheet">
<style>
  :root {
    --backdrop: #e4e5e7;
    --card-front: #ffffff;
    --card-back: #f7f7f5;
    --bronze: #7b5224;
    --ink: #2a2118;
    --emblem: #2b1f16;
    --emblem-ring: #231a13;
  }
  * { margin: 0; padding: 0; box-sizing: border-box; }
  html, body {
    width: 1200px;
    height: 720px;
    overflow: hidden;
    background: var(--backdrop);
    font-family: "Gelasio", Georgia, serif;
  }
  .stage { position: relative; width: 1200px; height: 720px; }
  .card {
    position: absolute;
    top: 240px;
    width: 420px;
    height: 240px;
    overflow: hidden;
  }
  .card--front { left: 147px; background: var(--card-front); }
  .card--back  { left: 633px; background: var(--card-back); }
  .card svg.art { position: absolute; inset: 0; }

  .edge-tab {
    position: absolute;
    left: 0; top: 28px;
    width: 16px; height: 186px;
    background: var(--bronze);
    border-radius: 0 12px 12px 0;
  }
  .person { position: absolute; left: 51px; top: 33px; }
  .person__name {
    font-weight: 700;
    font-size: 16px;
    letter-spacing: 0.3px;
    color: var(--bronze);
    line-height: 18px;
  }
  .person__role { font-size: 12.5px; color: var(--ink); line-height: 14px; }
  .address {
    position: absolute; left: 51px; top: 86px;
    font-size: 12.5px; line-height: 16px; color: var(--ink);
    font-style: normal;
  }
  .contacts { position: absolute; left: 51px; top: 148px; list-style: none; }
  .contacts li {
    display: flex; align-items: center; gap: 6px;
    font-size: 12.5px; line-height: 18px; color: var(--ink);
  }
  .contacts svg { width: 13px; height: 13px; flex: none; }

  .brand {
    position: absolute;
    left: 0; width: 100%;
    top: 152px;
    padding-left: 166px;
    text-align: center;
    font-weight: 700;
    font-size: 26px;
    letter-spacing: 1px;
    color: var(--ink);
  }
</style>
</head>
<body>
<main class="stage">

  <section class="card card--front">
    <svg class="art" width="420" height="240" viewBox="0 0 420 240" role="img" aria-label="Brand emblem area, left half">
      <circle cx="420" cy="121" r="119" fill="none" stroke="var(--emblem-ring)" stroke-width="3"/>
      <circle cx="420" cy="121" r="113" fill="var(--emblem)"/>
    </svg>
    <div class="edge-tab"></div>
    <div class="person">
      <p class="person__name">COLIN VEY</p>
      <p class="person__role">Partner</p>
    </div>
    <address class="address">7C, Brennick Road,<br>Wan Chai,<br>Hong Kong</address>
    <ul class="contacts">
      <li>
        <svg viewBox="0 0 16 16" aria-hidden="true"><path fill="var(--bronze)" d="M1 6c0-3 3-4 7-4s7 1 7 4l-3 1-1-2H5L4 7 1 6zm3 2h8l2 6H2l2-6zm4 1.5a2 2 0 1 0 0 4 2 2 0 0 0 0-4z"/></svg>
        +852 9703 5164
      </li>
      <li>
        <svg viewBox="0 0 16 16" aria-hidden="true"><rect x="1" y="3" width="14" height="10" fill="none" stroke="var(--bronze)" stroke-width="1.6"/><path d="M1 3l7 6 7-6M1 13l5-5M15 13l-5-5" fill="none" stroke="var(--bronze)" stroke-width="1.4"/></svg>
        xxx@zanquorra.com
      </li>
      <li>
        <svg viewBox="0 0 16 16" aria-hidden="true"><g fill="none" stroke="var(--bronze)" stroke-width="1.3"><circle cx="8" cy="8" r="6.5"/><ellipse cx="8" cy="8" rx="3" ry="6.5"/><path d="M1.5 8h13M2.5 5h11M2.5 11h11"/></g></svg>
        www.zanquorra.com
      </li>
    </ul>
  </section>

  <section class="card card--back">
    <svg class="art" width="420" height="240" viewBox="0 0 420 240" role="img" aria-label="Brand emblem area, right half">
      <circle cx="0" cy="121" r="119" fill="none" stroke="var(--emblem-ring)" stroke-width="3"/>
      <circle cx="0" cy="121" r="113" fill="var(--emblem)"/>
      <circle cx="293" cy="104" r="45" fill="none" stroke="var(--emblem-ring)" stroke-width="2.5"/>
    </svg>
    <p class="brand">ZANQUORRA</p>
  </section>

</main>
</body>
</html>
```